Savor and Thrive Wellbeing is being Launched and needs a business card and stationery package

I need a stationery package including business card (primary focus) , letterhead, digital letterhead, envelopes, with compliments slip, A 5 note sheet for the rebranding of my business and launch of my new website. I have a logo, like beige, brown earthy tones with a hint of red. I would also like the option of my letterhead also being printed on recycled paper in another format as well as the traditional letterhead. I do also send my letters to GPs and specialists digitally as well. I like to stand out from the usual stereotype of fruits and vegetables on business cards as I find that quite tacky and stereotypical. I want the business card to capture the essence of my logo as natural, nutrition, enjoyment, nurturing and freedom with food. I have attached the logo, and additional brief sheet on my ideas. Happy to have any background that is complementary to my theme, and what you believe would be catching. Definitely DONT'T like pink, try to pick up the darker colour in the logo please. and think too much black is a little overpowering.

Target Market(s)

clients who are interested in improving their health and wellness. Client 80% females; 20% males

Industry/Entity Type

Health And Wellness

Contact Information for Business Card

I am open to having different backgrounds as well that would complement the logo. Probably less emphasis on the heart out of the logo - just happy to keep that in the logo only please
I am also wanting two business cards - one for the appointments, one for general distribution and media distribution (both need to look consistent though) - but does give opportunity for one of the business cards to be less wordy and more striking. And the front of the business card can certainly stand out with the entire savor and thrive logo and my name and grab the attention of the receiver.
1st business card
on front:
Imogen Whitcombe
Savor and Thrive Wellbeing & logo
Nutritionist and Dietitian
Tolva Medical Centre
364 Wexley Park Rd, Carina Q 4152
Phone: (07) 3521 7094 Fax: (07) 3617 2289
Mobile: 0400 915 268
www.savorandthrivewellbeing.example
imogen@savorandthrivewellbeing.example
on back:
next appointment

……………………….. at ……………………… (possibly 4 times)
If you are unable to keep your appointment, please contact us as soon as possible (small font)
2nd business card (needs to be very eye catching and stand out)
on front: Savor and Thrive Wellbeing logo and my name
on back:
Imogen Whitcombe
address
phones, fax, website, email address

Font styles to use
Other font styles liked:
• please refer to logo

Requirements
Must have
• refreshing and simple; new and vibrant - I am rebranding my business after 20 years
• to get a feel of what is the theme - go to my new website (not completed as yet - but you will get a preliminary view) - don't do as google search as blocked - but can put into website header and it will be shown
• www.savorandthrivewellbeing.example - but please ignore the colouring of the 4 blocks under the slider on the home page - I am not wanting these colourings - they are getting updated.
Nice to have
• earthy tones, beige, hint of red, fonts to match logo if possible, organic, modern
• get inspiration from my logo please, open to having other backgrounds that complement
Should not have
• no food shots or stereotypical weight/ scales images
• no green, yellow or orange

```html
<!DOCTYPE html>
<html lang="en">
<head>
<meta charset="utf-8">
<title>Savor and Thrive Wellbeing – Business Cards</title>
<link href="https://fonts.googleapis.com/css2?family=Open+Sans:wght@400;600;700&display=swap" rel="stylesheet">
<style>
  :root {
    --backdrop: #ece6de;
    --card: #ffffff;
    --rose: #b8646d;
    --plum: #3b3035;
    --ink: #3a3a3a;
    --ink-soft: #5a5a5a;
    --dots: #6a6a6a;
  }
  * { box-sizing: border-box; margin: 0; padding: 0; }
  html, body {
    width: 1200px; height: 900px; overflow: hidden;
    background: var(--backdrop);
    font-family: "Open Sans", Arial, sans-serif;
    color: var(--ink);
  }
  .card {
    position: absolute;
    width: 560px; height: 320px;
    background: var(--card);
    box-shadow: 0 10px 26px rgba(60, 45, 40, 0.18);
    overflow: hidden;
  }
  /* Appointment card (back) */
  .appointment-card { left: 70px; top: 90px; }
  .appointment-card .band-top,
  .appointment-card .band-bottom { position: absolute; left: 0; right: 0; background: var(--rose); }
  .appointment-card .band-top { top: 0; height: 16px; }
  .appointment-card .band-bottom { bottom: 0; height: 26px; }
  .appointment-heading { position: absolute; left: 60px; top: 46px; }
  .appointment-heading .kicker { font-size: 12px; letter-spacing: 0.3px; color: var(--ink-soft); }
  .appointment-heading .title { font-size: 32px; font-weight: 400; line-height: 1.05; color: var(--ink); }
  .appointment-lines { position: absolute; left: 60px; right: 40px; top: 104px; }
  .appointment-row {
    display: flex; align-items: flex-end; gap: 12px;
    height: 34px;
  }
  .appointment-row .dotted { flex: 1; border-bottom: 2px dotted var(--dots); height: 1px; margin-bottom: 4px; }
  .appointment-row .at { font-size: 12px; color: var(--ink-soft); }
  .appointment-note {
    position: absolute; left: 60px; right: 40px; bottom: 36px;
    font-size: 12.5px; color: var(--ink-soft);
  }

  /* Contact card (front) */
  .contact-card { left: 570px; top: 470px; }
  .contact-card .band-top,
  .contact-card .band-bottom { position: absolute; left: 0; right: 0; background: var(--plum); }
  .contact-card .band-top { top: 0; height: 14px; }
  .contact-card .band-bottom { bottom: 0; height: 40px; }
  .contact-details { position: absolute; left: 40px; top: 46px; }
  .person-name { font-size: 17px; font-weight: 700; color: var(--ink); }
  .person-role { font-size: 12.5px; color: var(--ink-soft); margin-left: 6px; }
  .practice-address { margin: 14px 0 0 22px; font-size: 13px; line-height: 1.35; color: var(--ink-soft); }
  .contact-list { list-style: none; margin: 16px 0 0 22px; }
  .contact-list li {
    display: flex; align-items: center; gap: 9px;
    font-size: 12.5px; line-height: 17px; color: var(--ink-soft);
  }
  .contact-list svg { width: 11px; height: 11px; fill: var(--ink); flex: none; }
  .brand-name {
    position: absolute; right: 40px; top: 108px; width: 210px;
    display: flex; align-items: center; gap: 10px;
  }
  .brand-name .dot { width: 14px; height: 14px; border-radius: 50%; background: var(--rose); flex: none; }
  .brand-name .wordmark { font-size: 21px; font-weight: 600; line-height: 1.2; color: var(--plum); }
</style>
</head>
<body>

<section class="card appointment-card" aria-label="Appointment card">
  <div class="band-top"></div>
  <div class="appointment-heading">
    <p class="kicker">YOUR NEXT</p>
    <h2 class="title">Appointment</h2>
  </div>
  <div class="appointment-lines">
    <div class="appointment-row"><span class="dotted"></span><span class="at">at</span><span class="dotted"></span></div>
    <div class="appointment-row"><span class="dotted"></span><span class="at">at</span><span class="dotted"></span></div>
    <div class="appointment-row"><span class="dotted"></span><span class="at">at</span><span class="dotted"></span></div>
    <div class="appointment-row"><span class="dotted"></span><span class="at">at</span><span class="dotted"></span></div>
  </div>
  <p class="appointment-note">If you are unable to keep your appointment, please contact us as soon as possible</p>
  <div class="band-bottom"></div>
</section>

<section class="card contact-card" aria-label="Contact card">
  <div class="band-top"></div>
  <div class="contact-details">
    <h1 class="person-name">Imogen Whitcombe</h1>
    <p class="person-role">Nutritionist and Dietitian</p>
    <p class="practice-address">Tolva Medical Centre<br>364 Wexley Park Rd,<br>Carina Q 4152</p>
    <ul class="contact-list">
      <li><svg viewBox="0 0 12 12"><path d="M1 4c0-2 2-3 5-3s5 1 5 3v1H8V4H4v1H1zM3 6h6l2 5H1z"/></svg>(07) 3521 7094</li>
      <li><svg viewBox="0 0 12 12"><path d="M3 1h5v3H3zM1 4h10v7H1zM3 6v1h2V6zm4 0v1h2V6zM3 8v1h2V8zm4 0v1h2V8z"/></svg>(07) 3617 2289</li>
      <li><svg viewBox="0 0 12 12"><path d="M3 0h6v12H3zm1 1v8h4V1zm2 9a.7.7 0 100 1.4A.7.7 0 006 10z"/></svg>0400 915 268</li>
      <li><svg viewBox="0 0 12 12"><path d="M0 2h12v8H0zm1 1l5 4 5-4z"/></svg>www.savorandthrivewellbeing.example</li>
      <li><svg viewBox="0 0 12 12"><circle cx="6" cy="6" r="5.5"/></svg>imogen@savorandthrivewellbeing.example</li>
    </ul>
  </div>
  <div class="brand-name">
    <span class="dot"></span>
    <span class="wordmark">Savor and Thrive Wellbeing</span>
  </div>
  <div class="band-bottom"></div>
</section>

</body>
</html>
```